BUSINESS CARDS, ENVELOPE, LETTER HEADS AND OTHER STATIONARY
FOR BROOKFERN DATA TECHNOLOGY
I need double sided standard sized Business Card [3.5" x 2"]
Please show me a wide variey of fonts including the ones from the logo
Bright & Fun-filled
Dorian Velmont
Solutions Architect / Technical Sales
82 Pinewhistle Crescent SW
Calgary, Alberta
Canada T2K7M5
dorianv@brookferndataworks.example
http://www.brookferndataworks.example
On the Back of the Bussiness Card I would like to describe a few of the features and solutions that Brookfern Data provides like:
- Electronic Records Management
-IT Solutions (Hardware / Software)
- After hours Technical support (Disaster Recover)
- Procurement
Logo
LOGO file 2
Please Do Not Include the Reflection as part of the logo Thank You

```html
<!DOCTYPE html>
<html lang="en">
<head>
<meta charset="utf-8">
<title>Brookfern Data Technology — Stationery Set</title>
<link href="https://fonts.googleapis.com/css2?family=Open+Sans:wght@400;600;700&display=swap" rel="stylesheet">
<style>
:root{
  --stage-light:#4a9be0;
  --stage-dark:#1a5aa6;
  --brand-blue:#1f6fc4;
  --brand-blue-deep:#124f9a;
  --brand-green:#3aa83a;
  --brand-green-deep:#237a2a;
  --paper:#ffffff;
  --ink:#2a3f5c;
  --ink-soft:#7a8aa0;
  --line:#c9d6e6;
}
*{box-sizing:border-box;margin:0;padding:0}
html,body{width:1200px;height:506px;overflow:hidden}
body{font-family:"Open Sans",Arial,sans-serif;color:var(--ink);line-height:1.3}
.stage{position:relative;width:1200px;height:506px;overflow:hidden;
  background:radial-gradient(ellipse at 50% 40%,var(--stage-light),var(--stage-dark) 85%)}
.piece{position:absolute;overflow:hidden;box-shadow:0 3px 8px rgba(0,30,70,.35)}
.paper{background:var(--paper)}
.wave{position:absolute;left:0;width:100%}
.brand{display:flex;align-items:center;gap:5px;font-weight:700;color:var(--brand-blue-deep);white-space:nowrap;line-height:1}
.brand-dot{border-radius:50%;background:var(--brand-green);flex:none}
.watermark{position:absolute;border-radius:50%;background:rgba(31,111,196,.06)}
.tiny{font-size:4px;line-height:6px;color:var(--ink-soft);white-space:nowrap}

/* compliment slip & envelope */
.slip{left:30px;top:22px;width:120px;height:50px}
.flap-blue{left:30px;top:82px;width:272px;height:40px;background:linear-gradient(90deg,var(--brand-blue-deep),var(--brand-blue));border-radius:0 0 60% 40%/0 0 100% 60%}
.flap-green{left:30px;top:124px;width:272px;height:38px;background:linear-gradient(90deg,var(--brand-green-deep),var(--brand-green));border-radius:0 0 40% 60%/0 0 60% 100%}
.envelope{left:30px;top:172px;width:280px;height:126px}

/* letterhead */
.letter{left:320px;top:22px;width:232px;height:330px}
.letter-body{position:absolute;left:22px;top:40px;right:22px}
.letter-body p{height:3px;background:var(--line);margin-bottom:7px;border-radius:2px}

/* folder */
.folder{left:566px;top:22px;width:380px;height:330px;background:linear-gradient(160deg,var(--brand-blue),var(--brand-blue-deep));box-shadow:0 3px 10px rgba(0,30,70,.4)}
.folder-spine{position:absolute;left:190px;top:0;width:2px;height:100%;background:rgba(255,255,255,.25)}
.folder-pocket{position:absolute;left:190px;bottom:0;width:190px;height:110px;background:linear-gradient(180deg,#2b7fd0,var(--brand-blue-deep));border-top-left-radius:40px}
.slot-card{position:absolute;left:122px;top:268px;width:66px;height:38px;background:var(--paper);box-shadow:0 2px 5px rgba(0,30,70,.35)}

.letter-b{left:762px;top:26px;width:178px;height:292px}
.fax{left:958px;top:22px;width:214px;height:330px}
.fax-form{position:absolute;left:18px;top:62px;right:18px}
.fax-row{display:flex;gap:6px;margin-bottom:6px;font-size:5px;color:var(--ink)}
.fax-row span{flex:1;border-bottom:1px solid var(--line)}
.checks{display:flex;justify-content:space-between;margin-top:10px;font-size:4px;color:var(--ink)}
.checks i{display:inline-block;width:4px;height:4px;border:1px solid var(--ink-soft);margin-right:2px;vertical-align:middle}

/* business cards */
.card{top:366px;width:176px;height:100px}
.card-front{background:var(--paper)}
.card-blue{background:linear-gradient(135deg,#3a8ee0,var(--brand-blue-deep))}
.card-green{background:linear-gradient(135deg,#5cc24a,var(--brand-green-deep))}
.card .front-brand{position:absolute;left:10px;top:12px}
.card .details{position:absolute;left:10px;top:34px;display:flex;flex-direction:column;gap:1px}
.card .name{font-size:6px;line-height:8px;font-weight:700;color:var(--brand-blue-deep)}
.card .role{font-size:4.5px;line-height:6px;color:var(--ink-soft);margin-bottom:3px}
.card .features{position:absolute;left:14px;top:30px;color:#fff;font-size:5px;line-height:8px;list-style:none}
.card .features li::before{content:"• "}
.card .back-brand{position:absolute;left:14px;top:12px}
.card .back-brand .brand{color:#fff}
</style>
</head>
<body>
<main class="stage">

  <!-- compliment slip -->
  <section class="piece paper slip">
    <div class="brand" style="position:absolute;left:30px;top:20px;font-size:6px"><span class="brand-dot" style="width:9px;height:9px"></span>Brookfern Data</div>
  </section>

  <!-- envelope back flaps -->
  <section class="piece flap-blue">
    <span class="brand-dot" style="position:absolute;left:126px;top:14px;width:8px;height:8px;display:block"></span>
  </section>
  <section class="piece flap-green">
    <span class="brand-dot" style="position:absolute;left:126px;top:12px;width:8px;height:8px;display:block;background:#fff"></span>
  </section>

  <!-- envelope front -->
  <section class="piece paper envelope">
    <div class="brand" style="position:absolute;left:14px;top:14px;font-size:10px"><span class="brand-dot" style="width:14px;height:14px"></span>Brookfern Data</div>
    <div class="tiny" style="position:absolute;left:14px;top:34px">82 Pinewhistle Crescent SW, Calgary, Alberta T2K7M5</div>
    <svg class="wave" style="bottom:0;height:34px" viewBox="0 0 280 34" preserveAspectRatio="none">
      <path d="M0 18 C90 4 180 32 280 12 V34 H0Z" fill="var(--brand-blue)"/>
      <path d="M0 25 C100 14 190 36 280 21 V34 H0Z" fill="var(--brand-green)"/>
    </svg>
  </section>

  <!-- letterhead -->
  <section class="piece paper letter">
    <div class="watermark" style="width:170px;height:170px;left:40px;top:80px"></div>
    <div class="letter-body"><p></p><p style="width:80%"></p><p></p><p></p><p style="width:60%"></p></div>
    <svg class="wave" style="bottom:0;height:52px" viewBox="0 0 232 52" preserveAspectRatio="none">
      <path d="M0 20 C70 6 150 38 232 12 V52 H0Z" fill="var(--brand-blue)"/>
      <path d="M0 30 C80 20 160 46 232 26 V52 H0Z" fill="var(--brand-green)"/>
    </svg>
    <div class="tiny" style="position:absolute;left:14px;bottom:8px;color:#fff">(403) 555-0142 · dorianv@brookferndataworks.example · www.brookferndataworks.example</div>
  </section>

  <!-- presentation folder -->
  <section class="piece folder">
    <div class="watermark" style="width:170px;height:170px;left:205px;top:40px;background:rgba(255,255,255,.07)"></div>
    <div class="folder-spine"></div>
    <span class="brand-dot" style="position:absolute;left:74px;top:120px;width:22px;height:22px;display:block"></span>
    <div class="tiny" style="position:absolute;left:40px;top:158px;width:110px;color:#dfeaf7;text-align:center">82 Pinewhistle Crescent SW<br>Calgary, Alberta T2K7M5<br>(403) 555-0142<br>www.brookferndataworks.example</div>
    <div class="folder-pocket"></div>
    <div class="slot-card">
      <div class="brand" style="position:absolute;left:6px;top:15px;font-size:4.5px"><span class="brand-dot" style="width:6px;height:6px"></span>Brookfern Data</div>
    </div>
  </section>

  <!-- letterhead in folder pocket -->
  <section class="piece paper letter-b">
    <div class="watermark" style="width:130px;height:130px;left:24px;top:100px"></div>
    <div class="brand" style="position:absolute;left:14px;top:14px;font-size:10px"><span class="brand-dot" style="width:14px;height:14px"></span>Brookfern Data</div>
    <div class="tiny" style="position:absolute;left:14px;top:34px">82 Pinewhistle Crescent SW · Calgary, Alberta</div>
    <svg class="wave" style="bottom:0;height:36px" viewBox="0 0 178 36" preserveAspectRatio="none">
      <path d="M0 16 C60 4 120 30 178 10 V36 H0Z" fill="var(--brand-blue)"/>
      <path d="M0 25 C60 16 120 38 178 21 V36 H0Z" fill="var(--brand-green)"/>
    </svg>
  </section>

  <!-- fax sheet -->
  <section class="piece paper fax">
    <div class="watermark" style="width:150px;height:150px;left:32px;top:140px"></div>
    <div class="brand" style="position:absolute;left:16px;top:16px;font-size:11px"><span class="brand-dot" style="width:15px;height:15px"></span>Brookfern Data</div>
    <div style="position:absolute;right:16px;top:20px;font-size:9px;font-weight:700;color:var(--brand-blue-deep)">FAX</div>
    <div class="fax-form">
      <div class="fax-row">To:<span></span>From:<span></span></div>
      <div class="fax-row">Fax:<span></span>Pages:<span></span></div>
      <div class="fax-row">Phone:<span></span>Date:<span></span></div>
      <div class="fax-row">Re:<span></span></div>
      <div class="checks"><span><i></i>Urgent</span><span><i></i>For Review</span><span><i></i>Please Comment</span><span><i></i>Please Reply</span></div>
    </div>
    <svg class="wave" style="bottom:0;height:40px" viewBox="0 0 214 40" preserveAspectRatio="none">
      <path d="M0 18 C70 6 140 34 214 12 V40 H0Z" fill="var(--brand-blue)"/>
      <path d="M0 27 C70 18 140 42 214 23 V40 H0Z" fill="var(--brand-green)"/>
    </svg>
  </section>

  <!-- business cards, set one -->
  <article class="piece card card-front" style="left:22px">
    <div class="watermark" style="width:84px;height:84px;left:86px;top:8px"></div>
    <div class="front-brand"><div class="brand" style="font-size:8px"><span class="brand-dot" style="width:12px;height:12px"></span>Brookfern Data</div></div>
    <div class="details">
      <div class="name">Dorian Velmont</div>
      <div class="role">Solutions Architect / Technical Sales</div>
      <div class="tiny">82 Pinewhistle Crescent SW<br>Calgary, Alberta, Canada T2K7M5<br>dorianv@brookferndataworks.example<br>http://www.brookferndataworks.example</div>
    </div>
    <svg class="wave" style="bottom:0;height:12px" viewBox="0 0 176 12" preserveAspectRatio="none"><path d="M0 7 C60 0 120 12 176 3 V12 H0Z" fill="var(--brand-blue)"/><path d="M0 9 C60 5 120 14 176 7 V12 H0Z" fill="var(--brand-green)"/></svg>
  </article>
  <article class="piece card card-blue" style="left:206px">
    <div class="back-brand"><div class="brand" style="font-size:7px"><span class="brand-dot" style="width:11px;height:11px"></span>Brookfern Data</div></div>
    <ul class="features"><li>Electronic Records Management</li><li>IT Solutions (Hardware / Software)</li><li>After Hours Technical Support (Disaster Recovery)</li><li>Procurement</li></ul>
  </article>
  <article class="piece card card-green" style="left:390px">
    <div class="back-brand"><div class="brand" style="font-size:7px"><span class="brand-dot" style="width:11px;height:11px;background:#fff"></span>Brookfern Data</div></div>
    <ul class="features"><li>Electronic Records Management</li><li>IT Solutions (Hardware / Software)</li><li>After Hours Technical Support (Disaster Recovery)</li><li>Procurement</li></ul>
  </article>

  <!-- business cards, set two -->
  <article class="piece card card-front" style="left:580px">
    <div class="watermark" style="width:84px;height:84px;left:86px;top:8px"></div>
    <div class="front-brand"><div class="brand" style="font-size:8px"><span class="brand-dot" style="width:12px;height:12px"></span>Brookfern Data</div></div>
    <div class="details">
      <div class="name">Dorian Velmont</div>
      <div class="role">Solutions Architect / Technical Sales</div>
      <div class="tiny">82 Pinewhistle Crescent SW<br>Calgary, Alberta, Canada T2K7M5<br>dorianv@brookferndataworks.example<br>http://www.brookferndataworks.example</div>
    </div>
    <svg class="wave" style="bottom:0;height:12px" viewBox="0 0 176 12" preserveAspectRatio="none"><path d="M0 5 C60 0 120 12 176 3 V12 H0Z" fill="var(--brand-blue)"/><path d="M0 8 C60 4 120 13 176 6 V12 H0Z" fill="var(--brand-green)"/></svg>
  </article>
  <article class="piece card card-blue" style="left:764px">
    <div class="back-brand"><div class="brand" style="font-size:7px"><span class="brand-dot" style="width:11px;height:11px"></span>Brookfern Data</div></div>
    <ul class="features"><li>Electronic Records Management</li><li>IT Solutions (Hardware / Software)</li><li>After Hours Technical Support (Disaster Recovery)</li><li>Procurement</li></ul>
  </article>
  <article class="piece card card-green" style="left:948px">
    <div class="back-brand"><div class="brand" style="font-size:7px"><span class="brand-dot" style="width:11px;height:11px;background:#fff"></span>Brookfern Data</div></div>
    <ul class="features"><li>Electronic Records Management</li><li>IT Solutions (Hardware / Software)</li><li>After Hours Technical Support (Disaster Recovery)</li><li>Procurement</li></ul>
  </article>

</main>
</body>
</html>
```